Milk product packaging

We are ready to begin packaging our product! Exciting! I already have a logo (from Pixel Forge!) and company name (Calbrin Ventures), but now we need an attractive, attention-drawing and pleasing package design. The product is a healthy flavored milk that needs to appeal to kids from 2 years old and up, moms shopping for kids, and potentially other adults. A hard task, but we don't want to limit the product to kids even though they will be the first customer we will advertise to.

The product will most likely be a flexa bok single serving milk package, like the kind kids take in their lunch boxes, that has a straw attached. It will need to have space for nutritional labeling and space on the back for advertising or things like 'fun facts.'

So far our main logo colors are green, black and white (see the logos attached.) Looking at competitors (Kestrel Organics, Zuba Milk, Bramlow Fields) they have used components of farms or cows on their products to appeal to a down-to-earth feel and to promote the idea of a product 'straight from the farm.' This isn't a necessity for me but it was something I noted. There will be multiple flavors of milk, and so far I've been using a bluish purple color for the Radiance blend (which contains blue and purple berries) and a dark yellow for the Calmora blend, an accent to the standard black/white/green color scheme of the logo and materials. So all packages look the same, but a different flavor has a different 'splash' of color to differentiate it. Again, just my thoughts and i'm open to other looks and ideas. We're advertising it as "milk plus a nourishing blend of ....." Statistics say we only have 3-5 seconds to influence the customer to pick up and try our product, so we're looking for a winning design to help us do just that!! We want to lead the way in flavored milk that is healthy, not just added sugar and artificial ingredients. The attached files are the logos we got from Pixel Forge. Healthy, nourishing, flavored milk!

Reason: Hi! Many designers seem to be busy...just seeing if this helps. So far I love the ideas I'm seeing! Thanks.

```html
<!DOCTYPE html>
<html lang="en">
<head>
<meta charset="utf-8">
<title>Calbrin Ventures – Organic Milk Carton Dielines</title>
<link href="https://fonts.googleapis.com/css2?family=Quicksand:wght@700&family=Pacifico&family=Patrick+Hand&family=Roboto+Condensed:ital,wght@0,400;0,700;1,700&display=swap" rel="stylesheet">
<style>
  :root {
    --leaf-green: #9cc93b;
    --navy: #16233a;
    --white: #ffffff;
    --peach: #f4c9a8;
    --cream: #f6dc8c;
    --panel-line: rgba(0,0,0,0.12);
  }
  * { box-sizing: border-box; margin: 0; padding: 0; }
  html, body { width: 986px; height: 1200px; overflow: hidden; background: #ffffff; }
  body { position: relative; font-family: "Roboto Condensed", Arial, sans-serif; color: var(--navy); }

  .carton { position: absolute; left: 19px; width: 948px; height: 560px; overflow: hidden;
            box-shadow: 0 6px 14px rgba(0,0,0,0.18); background: var(--white); }
  .carton--berry { top: 24px; --splash: #0fa6e2; --base: #6a2a8e; }
  .carton--calm  { top: 596px; --splash: #5b3a1e; --base: #e8922a; }

  .carton__art { position: absolute; inset: 0; width: 948px; height: 560px; }
  .splash { fill: var(--splash); }
  .base { fill: var(--base); stroke: var(--white); stroke-width: 3; }
  .band { fill: var(--leaf-green); }

  .panel { position: absolute; top: 0; width: 237px; height: 560px; border-left: 1px solid var(--panel-line); }
  .panel--side { left: 0; border-left: none; }
  .panel--front-a { left: 237px; }
  .panel--back { left: 474px; }
  .panel--front-b { left: 711px; }

  .best-before { position: absolute; left: 12px; top: 62px; color: var(--white);
                 font-family: "Patrick Hand", cursive; font-size: 13px; display: flex; align-items: flex-end; gap: 4px; white-space: nowrap; }
  .best-before__line { display: inline-block; width: 150px; border-bottom: 1px solid var(--white); height: 12px; }

  /* nutrition */
  .nutrition { position: absolute; left: 60px; top: 110px; width: 176px; height: 358px; background: var(--white);
               padding: 8px 8px; color: #111; font-size: 7.5px; line-height: 1.3; white-space: nowrap; }
  .nutrition__title { font-weight: 700; font-size: 31px; line-height: 0.95; letter-spacing: -0.5px; }
  .nutrition__rule { border-top: 2px solid #111; margin: 4px 0 3px; }
  .nutrition__rule--thin { border-top-width: 1px; }
  .nutrition__row { display: flex; justify-content: space-between; font-weight: 700; font-size: 8.5px; }
  .nutrition__row span:last-child, .nutrition__line span:last-child { width: 62px; }
  .nutrition__line { display: flex; justify-content: space-between; }
  .nutrition__line--indent span:first-child { padding-left: 6px; }
  .nutrition__head { display: flex; justify-content: space-between; font-weight: 700; font-size: 7px; }
  .nutrition__head span:last-child { width: 62px; }

  .recycle-marks { position: absolute; left: 14px; top: 518px; display: flex; gap: 10px; }
  .recycle-marks span { width: 20px; height: 20px; border-radius: 50%; border: 2px solid var(--white); display: block; }

  /* front */
  .volume { position: absolute; left: 0; right: 0; top: 46px; text-align: center; color: var(--white);
            font-family: "Patrick Hand", cursive; font-size: 26px; }
  .brand-mark { position: absolute; left: 92px; top: 128px; width: 54px; height: 54px; border-radius: 50%; background: var(--leaf-green); }
  .brand-name { position: absolute; left: 0; right: 0; top: 198px; text-align: center;
                font-family: "Quicksand", sans-serif; font-weight: 700; font-size: 21px; color: var(--navy); white-space: nowrap; }
  .natural-tag { position: absolute; left: 128px; top: 302px; width: 56px; text-align: center; transform: rotate(-22deg);
                 font-family: "Pacifico", cursive; font-size: 11px; line-height: 1.05; color: var(--white); }
  .product-name { position: absolute; left: 18px; top: 338px; font-family: "Pacifico", cursive; font-size: 40px; color: var(--white); line-height: 1.3; }
  .product-rule { position: absolute; left: 12px; top: 411px; width: 150px; height: 2px; background: var(--white); }
  .benefits { position: absolute; left: 14px; top: 420px; list-style: none; color: var(--white);
              font-family: "Quicksand", sans-serif; font-weight: 700; font-size: 13px; line-height: 18px; }
  .benefits li::before { content: "• "; }
  .cream-badge { position: absolute; left: 146px; top: 404px; width: 88px; height: 88px; border-radius: 50%; background: var(--peach);
                 display: flex; flex-direction: column; align-items: center; justify-content: center; color: var(--navy);
                 font-family: "Quicksand", sans-serif; font-weight: 700; line-height: 0.95; text-align: center; }
  .cream-badge__big { font-size: 25px; }
  .cream-badge__small { font-size: 13px; margin-top: 2px; }
  .flavor { position: absolute; left: 18px; top: 506px; color: var(--cream); font-family: "Pacifico", cursive; white-space: nowrap; }
  .flavor__with { font-size: 11px; display: block; }
  .flavor__name { font-size: 17px; color: var(--white); line-height: 1.4; }
  .flavor__suffix { font-size: 10px; color: var(--white); }

  /* back */
  .info-title, .fact-title { position: absolute; left: 16px; font-weight: 700; font-style: italic; font-size: 14px; }
  .info-title { top: 118px; color: var(--navy); }
  .info-text, .fact-text { position: absolute; left: 16px; width: 208px; font-size: 9px; line-height: 13.5px; text-align: justify; }
  .info-text { top: 138px; color: var(--navy); }
  .fact-title { top: 318px; color: var(--white); }
  .fact-text { top: 340px; color: var(--white); }
  .contact-mark { position: absolute; left: 18px; top: 444px; width: 40px; height: 40px; border-radius: 50%; background: var(--leaf-green); }
  .contact { position: absolute; left: 64px; top: 446px; color: var(--white); font-size: 8.5px; line-height: 11px; font-weight: 700; white-space: nowrap; }
  .contact__social { display: flex; align-items: center; gap: 4px; margin-bottom: 3px; }
  .contact__social::before { content: ""; width: 9px; height: 9px; background: var(--white); display: block; }
  .contact__site { font-size: 11px; }
</style>
</head>
<body>

<section class="carton carton--berry" aria-label="Blue and Purple Berries carton">
  <svg class="carton__art" viewBox="0 0 948 560" preserveAspectRatio="none" aria-hidden="true">
    <rect class="band" x="0" y="0" width="948" height="103"/>
    <path class="splash" d="M0,258 Q120,236 237,262 Q356,288 474,262 Q592,236 711,262 Q830,288 948,258 L948,560 L0,560 Z"/>
    <path class="base" d="M0,496 Q60,470 120,490 T237,492 Q300,505 360,513 T474,514 Q540,520 590,512 T711,494 Q770,470 830,490 T948,494 L948,562 L0,562 Z"/>
  </svg>

  <div class="panel panel--side">
    <div class="best-before">Best Before : <span class="best-before__line"></span></div>
    <div class="nutrition">
      <div class="nutrition__title">Nutrition<br>Facts</div>
      <div class="nutrition__rule nutrition__rule--thin"></div>
      <div class="nutrition__row"><span>Serving Size</span><span>1 Sheet (2.5g)</span></div>
      <div class="nutrition__row"><span>Calories</span><span>10</span></div>
      <div class="nutrition__row"><span>Calories from Fat</span><span>0</span></div>
      <div class="nutrition__rule"></div>
      <div class="nutrition__head"><span>Amount Per Serving</span><span>% Daily Value (DV)*</span></div>
      <div class="nutrition__rule nutrition__rule--thin"></div>
      <div class="nutrition__line"><span>Total Fat 0g</span><span>0%</span></div>
      <div class="nutrition__line"><span>Saturated Fat 0g</span><span>0%</span></div>
      <div class="nutrition__line"><span>Trans Fat 0g</span><span>0%</span></div>
      <div class="nutrition__line"><span>Cholesterol 0mg</span><span>0%</span></div>
      <div class="nutrition__line"><span>Sodium 0mg</span><span>0%</span></div>
      <div class="nutrition__rule nutrition__rule--thin"></div>
      <div class="nutrition__line"><span>Vitamin A</span><span>6%</span></div>
      <div class="nutrition__line"><span>Vitamin C</span><span>4%</span></div>
      <div class="nutrition__head"><span>Amount Per Serving</span><span>% Daily Value (DV)*</span></div>
      <div class="nutrition__rule nutrition__rule--thin"></div>
      <div class="nutrition__line"><span>Total Carbohydrate 1g</span><span>0%</span></div>
      <div class="nutrition__line nutrition__line--indent"><span>Dietary Fiber 1g</span><span>3%</span></div>
      <div class="nutrition__line nutrition__line--indent"><span>Sugars 0g</span><span></span></div>
      <div class="nutrition__line nutrition__line--indent"><span>Protein 1g</span><span></span></div>
      <div class="nutrition__rule nutrition__rule--thin"></div>
      <div class="nutrition__line"><span>Calcium</span><span>2%</span></div>
      <div class="nutrition__line"><span>Iron</span><span>2%</span></div>
    </div>
    <div class="recycle-marks" role="img" aria-label="Recycling and litter symbols"><span></span><span></span></div>
  </div>

  <div class="panel panel--front-a">
    <div class="volume">750 Ml</div>
    <div class="brand-mark"></div>
    <div class="brand-name">Calbrin Ventures</div>
    <div class="natural-tag">100%<br>natural</div>
    <div class="product-name">Organic</div>
    <div class="product-rule"></div>
    <ul class="benefits"><li>High Calsium</li><li>High Protein</li><li>Low GI</li></ul>
    <div class="cream-badge"><span class="cream-badge__big">Full</span><span class="cream-badge__small">Cream<br>Milk</span></div>
    <div class="flavor"><span class="flavor__with">With</span><span class="flavor__name">Blue &amp; Purple</span> <span class="flavor__suffix">Berries</span></div>
  </div>

  <div class="panel panel--back">
    <div class="best-before">Best Before : <span class="best-before__line"></span></div>
    <div class="info-title">INFO :</div>
    <p class="info-text">Lorem ipsum dolor sit amet, consectetur adipisicing elit, sed do eiusmod tempor incididunt ut labore et dolore magna aliqua. Ut enim ad minim veniam, quis nostrud exercitation ullamco laboris nisi ut aliquip ex ea commodo consequat. Duis aute irure dolor in reprehenderit in voluptate velit esse cillum dolore eu fugiat nulla pariatur.</p>
    <div class="fact-title">FUN FACT :</div>
    <p class="fact-text">Sed ut perspiciatis unde omnis iste natus error sit voluptatem accusantium doloremque laudantium, totam rem aperiam, eaque ipsa quae ab illo inventore veritatis et quasi architecto beatae vitae dicta sunt explicabo.</p>
    <div class="contact-mark" role="img" aria-label="Mascot character artwork"></div>
    <div class="contact">
      <div class="contact__social">Friendsite.com/calbrinventures</div>
      <div>Go to <span class="contact__site">CalbrinVentures.com</span></div>
      <div>to learn more about our milk</div>
    </div>
  </div>

  <div class="panel panel--front-b">
    <div class="volume">750 Ml</div>
    <div class="brand-mark"></div>
    <div class="brand-name">Calbrin Ventures</div>
    <div class="natural-tag">100%<br>natural</div>
    <div class="product-name">Organic</div>
    <div class="product-rule"></div>
    <ul class="benefits"><li>High Calsium</li><li>High Protein</li><li>Low GI</li></ul>
    <div class="cream-badge"><span class="cream-badge__big">Full</span><span class="cream-badge__small">Cream<br>Milk</span></div>
    <div class="flavor"><span class="flavor__with">With</span><span class="flavor__name">Blue &amp; Purple</span> <span class="flavor__suffix">Berries</span></div>
  </div>
</section>

<section class="carton carton--calm" aria-label="Brown and orange carton">
  <svg class="carton__art" viewBox="0 0 948 560" preserveAspectRatio="none" aria-hidden="true">
    <rect class="band" x="0" y="0" width="948" height="103"/>
    <path class="splash" d="M0,258 Q120,236 237,262 Q356,288 474,262 Q592,236 711,262 Q830,288 948,258 L948,560 L0,560 Z"/>
    <path class="base" d="M0,496 Q60,470 120,490 T237,492 Q300,505 360,513 T474,514 Q540,520 590,512 T711,494 Q770,470 830,490 T948,494 L948,562 L0,562 Z"/>
  </svg>

  <div class="panel panel--side">
    <div class="best-before">Best Before : <span class="best-before__line"></span></div>
    <div class="nutrition">
      <div class="nutrition__title">Nutrition<br>Facts</div>
      <div class="nutrition__rule nutrition__rule--thin"></div>
      <div class="nutrition__row"><span>Serving Size</span><span>1 Sheet (2.5g)</span></div>
      <div class="nutrition__row"><span>Calories</span><span>10</span></div>
      <div class="nutrition__row"><span>Calories from Fat</span><span>0</span></div>
      <div class="nutrition__rule"></div>
      <div class="nutrition__head"><span>Amount Per Serving</span><span>% Daily Value (DV)*</span></div>
      <div class="nutrition__rule nutrition__rule--thin"></div>
      <div class="nutrition__line"><span>Total Fat 0g</span><span>0%</span></div>
      <div class="nutrition__line"><span>Saturated Fat 0g</span><span>0%</span></div>
      <div class="nutrition__line"><span>Trans Fat 0g</span><span>0%</span></div>
      <div class="nutrition__line"><span>Cholesterol 0mg</span><span>0%</span></div>
      <div class="nutrition__line"><span>Sodium 0mg</span><span>0%</span></div>
      <div class="nutrition__rule nutrition__rule--thin"></div>
      <div class="nutrition__line"><span>Vitamin A</span><span>6%</span></div>
      <div class="nutrition__line"><span>Vitamin C</span><span>4%</span></div>
      <div class="nutrition__head"><span>Amount Per Serving</span><span>% Daily Value (DV)*</span></div>
      <div class="nutrition__rule nutrition__rule--thin"></div>
      <div class="nutrition__line"><span>Total Carbohydrate 1g</span><span>0%</span></div>
      <div class="nutrition__line nutrition__line--indent"><span>Dietary Fiber 1g</span><span>3%</span></div>
      <div class="nutrition__line nutrition__line--indent"><span>Sugars 0g</span><span></span></div>
      <div class="nutrition__line nutrition__line--indent"><span>Protein 1g</span><span></span></div>
      <div class="nutrition__rule nutrition__rule--thin"></div>
      <div class="nutrition__line"><span>Calcium</span><span>2%</span></div>
      <div class="nutrition__line"><span>Iron</span><span>2%</span></div>
    </div>
    <div class="recycle-marks" role="img" aria-label="Recycling and litter symbols"><span></span><span></span></div>
  </div>

  <div class="panel panel--front-a">
    <div class="volume">750 Ml</div>
    <div class="brand-mark"></div>
    <div class="brand-name">Calbrin Ventures</div>
    <div class="natural-tag">100%<br>natural</div>
    <div class="product-name">Organic</div>
    <div class="product-rule"></div>
    <ul class="benefits"><li>High Calsium</li><li>High Protein</li><li>Low GI</li></ul>
    <div class="cream-badge"><span class="cream-badge__big">Full</span><span class="cream-badge__small">Cream<br>Milk</span></div>
    <div class="flavor"><span class="flavor__with">With</span><span class="flavor__name">Blue &amp; Purple</span> <span class="flavor__suffix">Berries</span></div>
  </div>

  <div class="panel panel--back">
    <div class="best-before">Best Before : <span class="best-before__line"></span></div>
    <div class="info-title">INFO :</div>
    <p class="info-text">Lorem ipsum dolor sit amet, consectetur adipisicing elit, sed do eiusmod tempor incididunt ut labore et dolore magna aliqua. Ut enim ad minim veniam, quis nostrud exercitation ullamco laboris nisi ut aliquip ex ea commodo consequat. Duis aute irure dolor in reprehenderit in voluptate velit esse cillum dolore eu fugiat nulla pariatur.</p>
    <div class="fact-title">FUN FACT :</div>
    <p class="fact-text">Sed ut perspiciatis unde omnis iste natus error sit voluptatem accusantium doloremque laudantium, totam rem aperiam, eaque ipsa quae ab illo inventore veritatis et quasi architecto beatae vitae dicta sunt explicabo.</p>
    <div class="contact-mark" role="img" aria-label="Mascot character artwork"></div>
    <div class="contact">
      <div class="contact__social">Friendsite.com/calbrinventures</div>
      <div>Go to <span class="contact__site">CalbrinVentures.com</span></div>
      <div>to learn more about our milk</div>
    </div>
  </div>

  <div class="panel panel--front-b">
    <div class="volume">750 Ml</div>
    <div class="brand-mark"></div>
    <div class="brand-name">Calbrin Ventures</div>
    <div class="natural-tag">100%<br>natural</div>
    <div class="product-name">Organic</div>
    <div class="product-rule"></div>
    <ul class="benefits"><li>High Calsium</li><li>High Protein</li><li>Low GI</li></ul>
    <div class="cream-badge"><span class="cream-badge__big">Full</span><span class="cream-badge__small">Cream<br>Milk</span></div>
    <div class="flavor"><span class="flavor__with">With</span><span class="flavor__name">Blue &amp; Purple</span> <span class="flavor__suffix">Berries</span></div>
  </div>
</section>

</body>
</html>
```